Marwick Jewelers New Website Design

This project is to provide a new design for an existing website. The existing website is marwickjewelers dot com . I have created a overview document that outlines all the details for the project. I do not need the design to be converted into HTML. I have a team for that already so please don't ask. I have a lot of images .. too many to upload here so they are on my dev server located at pinefoxstudio com slash marwick slash assets

Number of Pages Required

1 page

```html
<!DOCTYPE html>
<html lang="en">
<head>
<meta charset="utf-8">
<title>Marwick Jewelers</title>
<link href="https://fonts.googleapis.com/css2?family=Jost:wght@300;400;500&display=swap" rel="stylesheet">
<style>
:root{
  --teal:#5a9aa3;
  --ink:#111111;
  --text:#333333;
  --muted:#666666;
  --soft:#f4f4f4;
  --line:#d9d9d9;
  --white:#ffffff;
}
*{margin:0;padding:0;box-sizing:border-box}
html,body{width:1200px;height:4745px;overflow:hidden}
body{font-family:'Jost',sans-serif;color:var(--text);background:var(--white);position:relative}
.abs{position:absolute}
.photo{position:absolute}
.topbar{left:0;top:0;width:1200px;height:43px;background:var(--teal);color:var(--white);font-size:13px;text-align:center;line-height:43px;letter-spacing:.3px}
.header-link{font-size:13px;color:var(--ink);letter-spacing:.5px;display:flex;align-items:center;gap:6px}
.call{font-size:13px;color:var(--ink);line-height:21px}
.call span{color:var(--muted)}
.brand{left:450px;top:110px;width:300px;text-align:center}
.brand-name{font-size:36px;font-weight:400;color:var(--ink);letter-spacing:1px;display:flex;align-items:center;justify-content:center;gap:10px}
.brand-dot{width:10px;height:10px;border-radius:50%;background:var(--teal)}
.nav{left:0;top:228px;width:1200px;height:53px;border-top:1px solid var(--line);border-bottom:2px solid var(--line)}
.nav ul{list-style:none;display:flex;position:absolute;left:88px;top:0;height:51px;align-items:center;gap:0}
.nav li{font-size:15px;color:var(--ink);margin-right:28px;position:relative;height:51px;line-height:51px}
.nav li.active{color:var(--teal)}
.nav li.active::after{content:"";position:absolute;left:-4px;right:-4px;top:-1px;height:2px;background:var(--teal)}
.eyebrow{font-size:13px;letter-spacing:.5px;color:var(--ink);font-weight:500}
.hero-title{font-size:40px;line-height:48px;color:var(--ink);font-weight:400}
.btn{display:inline-block;background:var(--ink);color:var(--white);font-size:12px;letter-spacing:.5px;border-radius:26px;text-align:center}
.circle-btn{width:40px;height:40px;border-radius:50%;border:1.5px solid var(--teal);display:flex;align-items:center;justify-content:center;background:var(--white)}
.service{width:300px;text-align:center}
.service h3{font-size:15px;font-weight:400;letter-spacing:.8px;color:var(--ink);margin:18px 0 14px}
.service p{font-size:12.5px;line-height:17px;color:var(--muted)}
.section-title{font-size:34px;font-weight:400;color:var(--ink);letter-spacing:1px}
.card{background:var(--white);position:absolute}
.card .thumb{position:absolute;left:50%;top:50%;transform:translate(-50%,-50%)}
.card-name{font-size:15px;color:var(--ink);text-align:center}
.card-price{font-size:14px;color:var(--text);text-align:center;margin-top:12px}
.body-lead{font-size:13px;line-height:21px;color:var(--ink)}
.body-copy{font-size:12.5px;line-height:21px;color:var(--muted)}
.gift-box{background:var(--ink);color:var(--white);padding:72px 40px 0 40px}
.gift-box p{font-size:13px;line-height:21px;margin-bottom:20px}
.footer{left:0;top:4322px;width:1200px;height:423px;background:var(--ink);color:var(--white)}
.footer h4{font-size:19px;font-weight:400;position:absolute;top:80px}
.footer .col{position:absolute;top:140px;font-size:14px;line-height:35px;list-style:none}
.footer .info{position:absolute;left:822px;top:138px;font-size:14px;line-height:23px}
.footer .rule{position:absolute;left:87px;top:325px;width:1026px;height:1px;background:#555}
.social{width:28px;height:28px;border-radius:50%;background:var(--white);position:absolute;top:351px}
</style>
</head>
<body>

<div class="abs topbar">Together we'll find a piece that speaks from the heart.</div>

<!-- Header -->
<div class="abs header-link" style="left:87px;top:123px">
  <svg width="16" height="16" viewBox="0 0 16 16"><circle cx="7" cy="7" r="5.2" fill="none" stroke="#111" stroke-width="1.4"/><line x1="11" y1="11" x2="15" y2="15" stroke="#111" stroke-width="1.4"/></svg>SEARCH
</div>
<div class="abs call" style="left:198px;top:122px">CALL US: <span>555-214-3870(Phone)</span><br><span style="padding-left:63px">800-555-0192(Toll Free)</span></div>
<div class="abs brand">
  <div class="brand-name"><span class="brand-dot"></span>Marwick</div>
  <div style="font-size:12px;letter-spacing:8px;color:var(--muted);margin-top:4px">JEWELERS</div>
</div>
<div class="abs header-link" style="left:874px;top:123px">LOGIN</div>
<div class="abs header-link" style="left:947px;top:123px">WISHLIST</div>
<div class="abs header-link" style="left:1037px;top:121px">
  <svg width="16" height="17" viewBox="0 0 16 17"><path d="M2 6h12l-1 10H3z" fill="none" stroke="#111" stroke-width="1.3"/><path d="M5 6V4a3 3 0 0 1 6 0v2" fill="none" stroke="#111" stroke-width="1.3"/></svg>CART (0)
</div>

<nav class="abs nav">
  <ul>
    <li class="active">Company</li>
    <li style="margin-right:30px">Custom Jewelery Services <svg width="10" height="6" viewBox="0 0 10 6"><path d="M1 1l4 4 4-4" fill="none" stroke="#111" stroke-width="1.2"/></svg></li>
    <li>Jewelery Repair Services</li>
    <li>Resources</li>
    <li>Showcase</li>
    <li>Gallery</li>
    <li>Engraving &amp; Trophies</li>
    <li>Gift Ideas</li>
  </ul>
</nav>

<!-- Hero -->
<div class="photo" role="img" aria-label="Close-up of a couple holding hands, showing an engagement ring" style="left:0;top:281px;width:726px;height:429px;background:linear-gradient(120deg,#5a5a5a 0%,#b9b9b9 45%,#e6e6e6 70%,#9c9c9c 100%)"></div>
<div class="photo" role="img" aria-label="Lower edge of the hero photo" style="left:0;top:710px;width:87px;height:66px;background:linear-gradient(180deg,#a9a9a9,#c9c9c9)"></div>
<svg class="abs" style="left:780px;top:420px" width="260" height="270" viewBox="0 0 260 270"><path d="M20 150 C60 40 170 10 255 20" fill="none" stroke="#e2e2e2" stroke-width="1.2"/><path d="M30 170 C80 170 60 260 40 260" fill="none" stroke="#e2e2e2" stroke-width="1.2"/></svg>
<div class="abs eyebrow" style="left:538px;top:384px">MARWICK JEWELERS</div>
<div class="abs hero-title" style="left:538px;top:412px">Say It with a</div>
<div class="abs hero-title" style="left:588px;top:460px">Stone and leave</div>
<div class="abs hero-title" style="left:637px;top:508px">her speechless</div>
<div class="abs btn" style="left:663px;top:577px;width:127px;height:47px;line-height:47px">SHOP NOW</div>
<div class="photo" role="img" aria-label="Rose gold halo engagement ring on a display stand" style="left:982px;top:359px;width:218px;height:328px;background:linear-gradient(160deg,#6b5a48 0%,#c9b59c 45%,#e8dcc9 75%,#bfae98 100%)"></div>
<div class="abs circle-btn" style="left:815px;top:660px"><svg width="8" height="12" viewBox="0 0 8 12"><path d="M6 1L1 6l5 5" fill="none" stroke="#111" stroke-width="1.3"/></svg></div>
<div class="abs circle-btn" style="left:866px;top:660px"><svg width="8" height="12" viewBox="0 0 8 12"><path d="M2 1l5 5-5 5" fill="none" stroke="#111" stroke-width="1.3"/></svg></div>

<!-- Services -->
<div class="abs service" style="left:104px;top:762px">
  <svg width="48" height="48" viewBox="0 0 48 48" fill="none" stroke="#111" stroke-width="1.5"><circle cx="14" cy="36" r="5"/><circle cx="34" cy="36" r="5"/><path d="M17 32L34 8M31 32L14 8"/><circle cx="32" cy="14" r="2.5"/></svg>
  <h3>JEWELRY REPAIR</h3>
  <p>Jewelry was meant to be worn, not sit in a drawer. Bring your broken rings, necklaces, earrings and watches to your trusted hometown jeweler.</p>
</div>
<div class="abs service" style="left:455px;top:762px">
  <svg width="48" height="48" viewBox="0 0 48 48" fill="none" stroke="#111" stroke-width="1.5"><path d="M14 4h20v10H14zM22 14v30h6V14M18 20h4M18 26h4M18 32h4"/></svg>
  <h3>SIZING</h3>
  <p>Your first sizing is free when you purchase your ring at Marwick Jewelers. If you need a ring sized, whether you bought it from us or not, we can help you find the size that fits.</p>
</div>
<div class="abs service" style="left:808px;top:762px">
  <svg width="48" height="48" viewBox="0 0 48 48" fill="none" stroke="#111" stroke-width="1.5"><path d="M6 18l8-10h20l8 10-18 24z"/><path d="M6 18h36M14 8l6 10 4-10 4 10 6-10M20 18l4 24 4-24"/></svg>
  <h3>CUSTOM DESIGN</h3>
  <p>If you've inherited jewelry you'll never wear, we can recreate an entirely new piece while preserving the sentimental value of it.</p>
</div>

<!-- Features -->
<div class="abs" style="left:0;top:1049px;width:1200px;height:624px;background:var(--soft)"></div>
<div class="abs section-title" style="left:83px;top:1146px">Features Items</div>
<div class="card" style="left:87px;top:1257px;width:236px;height:216px"><div class="thumb" role="img" aria-label="Silver wristwatch with blue dial" style="width:160px;height:50px;background:linear-gradient(90deg,#b7b7bd,#e3e3e6,#b7b7bd);border-radius:6px"></div></div>
<div class="card" style="left:348px;top:1222px;width:236px;height:343px">
  <div role="img" aria-label="Rose gold bracelet with diamonds" style="position:absolute;left:30px;top:80px;width:176px;height:60px;border-radius:50%;border:6px solid #d8a48a"></div>
  <div class="card-name" style="position:absolute;left:0;right:0;top:256px">Gold + Diamond Bracelets</div>
  <div class="card-price" style="position:absolute;left:0;right:0;top:276px">$ 50.00 - $ 60.00</div>
</div>
<div class="card" style="left:612px;top:1257px;width:236px;height:216px"><div class="thumb" role="img" aria-label="White gold crossover diamond ring" style="width:130px;height:90px;background:radial-gradient(ellipse,#f2f2f2 30%,#c8c8c8 70%,#fff 100%);border-radius:50%"></div></div>
<div class="card" style="left:875px;top:1257px;width:236px;height:216px"><div class="thumb" role="img" aria-label="Silver ring with red heart stone" style="width:120px;height:80px;background:radial-gradient(circle at 55% 40%,#8a1e2a 12%,#e2e2e2 30%,#fff 70%);border-radius:50%"></div></div>
<div class="abs circle-btn" style="left:22px;top:1344px;border-color:var(--teal)"><svg width="8" height="12" viewBox="0 0 8 12"><path d="M6 1L1 6l5 5" fill="none" stroke="#111" stroke-width="1.3"/></svg></div>
<div class="abs circle-btn" style="left:1132px;top:1344px"><svg width="8" height="12" viewBox="0 0 8 12"><path d="M2 1l5 5-5 5" fill="none" stroke="#111" stroke-width="1.3"/></svg></div>

<!-- Resources -->
<div class="abs section-title" style="left:83px;top:1772px">Resources</div>
<div class="abs" style="left:87px;top:1834px;width:420px">
  <p class="body-lead">Lorem Ipsum is simply dummy text of the printing and typesetting industry. Lorem Ipsum has been the industry's standard dummy text ever since the 1500s</p>
  <p class="body-copy" style="margin-top:20px">when an unknown printer took a galley of type and scrambled it to make a type specimen book. It has survived not only five centuries, but also the leap into electronic typesetting, remaining essentially unchanged. It was popularised in the 1960s with the release of Letraset sheets containing Lorem Ipsum passages, and more recently with desktop publishing software like Aldus PageMaker including versions of Lorem Ipsum.</p>
</div>
<div class="abs btn" style="left:87px;top:2093px;width:127px;height:43px;line-height:43px">LEARN MORE</div>
<div class="photo" role="img" aria-label="Gold chevron ring with diamond crown setting" style="left:642px;top:1784px;width:472px;height:270px;background:radial-gradient(ellipse at 50% 45%,#e8d8a6 0%,#b89a58 40%,#6f6a55 80%,#8c8a7a 100%)"></div>
<div class="photo" role="img" aria-label="Champagne stone halo ring on black background" style="left:565px;top:1906px;width:168px;height:248px;background:radial-gradient(circle at 50% 55%,#c9a98c 0%,#3a3a3a 40%,#1f1f1f 100%)"></div>

<!-- Gift Ideas -->
<div class="abs" style="left:0;top:2923px;width:1200px;height:787px;background:var(--soft)"></div>
<div class="abs" style="left:0;top:2263px;width:526px;height:660px;background:var(--teal)"></div>
<div class="abs" style="left:526px;top:2317px;width:674px;height:606px;background:var(--teal)"></div>
<svg class="abs" style="left:620px;top:2317px" width="120" height="160" viewBox="0 0 120 160"><path d="M110 4C60 30 20 80 10 156" fill="none" stroke="#8fbcc2" stroke-width="1.3"/></svg>
<svg class="abs" style="left:1000px;top:2410px" width="70" height="70" viewBox="0 0 70 70" fill="#fff"><path d="M28 2l4 14 14 4-14 4-4 14-4-14-14-4 14-4z"/><path d="M52 24l2 8 8 2-8 2-2 8-2-8-8-2 8-2z"/><path d="M14 48l2 6 6 2-6 2-2 6-2-6-6-2 6-2z"/></svg>
<div class="abs section-title" style="left:85px;top:2394px;color:var(--white)">Gift Ideas</div>
<div class="abs" style="left:87px;top:2453px;font-size:14px;line-height:18px;color:var(--white)">From "will you?" to "I do" and every<br>momentous occasion</div>
<div class="abs gift-box" style="left:87px;top:2580px;width:412px;height:504px">
  <p>Lorem Ipsum is simply dummy text of the printing and typesetting industry. Lorem Ipsum has been the industry's standard dummy text ever since the 1500s</p>
  <p>when an unknown printer took a galley of type and scrambled it to make a type specimen book. It has survived not only five centuries, but also the leap into electronic typesetting, remaining essentially unchanged. It was popularised in the 1960s with the release of Letraset sheets containing Lorem Ipsum passages, and more recently with desktop publishing software like Aldus PageMaker including versions of Lorem Ipsum.</p>
  <div class="btn" style="background:var(--white);color:var(--ink);width:127px;height:43px;line-height:43px;margin-top:4px">SHOP NOW</div>
</div>
<div class="photo" role="img" aria-label="Engraved brass bell with wooden handle" style="left:526px;top:2471px;width:412px;height:505px;background:radial-gradient(ellipse at 55% 65%,#e0c46a 0%,#a98a36 35%,#6b5a2e 60%,#d8dcd4 100%)"></div>
<div class="photo" role="img" aria-label="Engraved crystal ornament" style="left:966px;top:2709px;width:148px;height:267px;background:linear-gradient(160deg,#5a6468,#c9d0d3 50%,#7f8a8e)"></div>

<!-- Engraving & Trophies -->
<div class="abs section-title" style="left:83px;top:3186px">Engraving &amp; Trophies</div>
<div class="card" style="left:87px;top:3293px;width:236px;height:216px"><div class="thumb" role="img" aria-label="Tall trophy with figure on top" style="width:50px;height:150px;background:linear-gradient(180deg,#c9a24a,#7a2a22 50%,#c9a24a)"></div></div>
<div class="card" style="left:348px;top:3258px;width:236px;height:343px">
  <div role="img" aria-label="Clear acrylic award on blue base" style="position:absolute;left:68px;top:52px;width:100px;height:140px;background:linear-gradient(180deg,#eef3f6,#b8c6cf 80%,#2a4d7a 90%,#222)"></div>
  <div class="card-name" style="position:absolute;left:0;right:0;top:256px">Acrylic Award</div>
  <div class="card-price" style="position:absolute;left:0;right:0;top:276px">$ 590.00 - $ 800.00</div>
</div>
<div class="card" style="left:612px;top:3293px;width:236px;height:216px"><div class="thumb" role="img" aria-label="Flame-shaped glass award on black base" style="width:90px;height:140px;background:linear-gradient(180deg,#f4f4f4,#d2d6d8 85%,#222 86%);border-radius:45px 45px 6px 6px"></div></div>
<div class="card" style="left:875px;top:3293px;width:236px;height:216px"><div class="thumb" role="img" aria-label="Wooden plaque with engraved plate" style="width:110px;height:145px;background:linear-gradient(135deg,#6b3a1c,#3a2a3a 50%,#6b3a1c)"></div></div>
<div class="abs circle-btn" style="left:22px;top:3380px;background:var(--soft)"><svg width="8" height="12" viewBox="0 0 8 12"><path d="M6 1L1 6l5 5" fill="none" stroke="#111" stroke-width="1.3"/></svg></div>
<div class="abs circle-btn" style="left:1132px;top:3380px;background:var(--soft)"><svg width="8" height="12" viewBox="0 0 8 12"><path d="M2 1l5 5-5 5" fill="none" stroke="#111" stroke-width="1.3"/></svg></div>

<!-- Gallery -->
<div class="abs section-title" style="left:0;width:1200px;text-align:center;top:3814px">Gallery</div>
<div class="photo" role="img" aria-label="Jeweled dragonfly pendant on a display bust" style="left:87px;top:3889px;width:236px;height:239px;background:radial-gradient(circle at 50% 45%,#6a3a6e 0%,#c9b38a 30%,#e8e2da 70%)"></div>
<div class="photo" role="img" aria-label="Crystal cross on fabric" style="left:350px;top:3889px;width:236px;height:239px;background:linear-gradient(135deg,#8a7a70,#e8e4e0 50%,#a39890)"></div>
<div class="photo" role="img" aria-label="Engraving machine work table" style="left:614px;top:3889px;width:237px;height:239px;background:linear-gradient(160deg,#2a2a2a,#9a9a9a 50%,#3a3a3a)"></div>
<div class="photo" role="img" aria-label="Ring with purple stone and coral petals" style="left:877px;top:3889px;width:238px;height:239px;background:radial-gradient(circle at 50% 45%,#5a2a7a 0%,#d88a70 25%,#9aa6ac 60%)"></div>
<div class="abs btn" style="left:536px;top:4167px;width:127px;height:45px;line-height:45px">VIEW ALL</div>

<!-- Footer -->
<footer class="abs footer">
  <h4 style="left:87px">Main Menu</h4>
  <ul class="col" style="left:87px"><li>Company</li><li>Custom Jewelery Services</li><li>Jewelery Repair Services</li><li>Resources</li></ul>
  <ul class="col" style="left:308px"><li>Showcase</li><li>Gallery</li><li>Engraving &amp; Trophies</li><li>Gift Ideas</li></ul>
  <h4 style="left:536px">Category</h4>
  <ul class="col" style="left:536px"><li>Rings</li><li>Quickshops</li><li>Pendants</li><li>Earrings</li></ul>
  <ul class="col" style="left:665px"><li>Diamonds</li><li>Gemstones</li></ul>
  <h4 style="left:822px">Contact Info</h4>
  <div class="info">
    <div style="margin-bottom:12px">Location: 48 Birch Ave N, Alderton, MN</div>
    <div>Phone: 555-214-3870</div>
    <div style="margin-bottom:12px">800-555-0192 (Toll Free)</div>
    <div>Store Hours:&nbsp; Mon-Fri: 8:00 AM - 5:00PM</div>
  </div>
  <div class="rule"></div>
  <div class="abs" style="left:87px;top:355px;font-size:14px">©2022 Marwick Jewelers: Minnesota Jeweler. All Rights Reserved.</div>
  <div class="social" style="left:1042px"></div>
  <div class="social" style="left:1086px"></div>
</footer>

</body>
</html>
```